Local massage therapist needs some new marketing material

Hi there! I am a massage therapist here in Denver, CO in Brindle Hollow(shopping and art district) of the city. My business is called Lunora Massage of Denver. My practice has an eastern influence and I do reflexology, thai massage and use Chinese herbs, etc. I know all my clients and pay close attention to details. I am also very respectful of tradition and it shows in how I work. I tend to like modern, clean, fun, Asian designs. I am wanting a new business card and brochure. I have a logo and branding for my business that I want used in the design. Currently, the sign for my building is purple and I think my logo was designed to be purple. I will attach pictures of it and can send whatever files are necessary so it can be integrated into the brochure, etc. I like the purple but open to using other colors as well. Thanks!
My website is lunoramassagestudio.example where info can be gathered about me and services/fees for brochure.
Updates

Just increased budget. Please see new feedback in discussion thread.

Thanks!

                                       HEY ALL,

Just wanted to let you know that I made a change to my website. It is on the Prices Page. I no longer have the frequent  flyer prices but I added discounts. Let me know if you have any questions. Thanks so much!

Target Market(s)

healthy, urban, educated, upper middle class, yogis

Industry/Entity Type

Marketing

Requirements
Must have
• logo stays purple
Should not have
• not too busy

```html
<!DOCTYPE html>
<html lang="en">
<head>
<meta charset="utf-8">
<title>Lunora – Business Card</title>
<link rel="stylesheet" href="https://fonts.googleapis.com/css2?family=Open+Sans:wght@400;600;700&display=swap">
<style>
  :root {
    --purple: #5b2c91;
    --charcoal: #333336;
    --ink: #3d3d40;
    --grey: #6b6b70;
    --rule: #b9b9be;
    --card: #ffffff;
    --backdrop: #eceae6;
  }
  * { box-sizing: border-box; margin: 0; padding: 0; }
  html, body {
    width: 1200px; height: 720px; overflow: hidden;
    background: var(--backdrop);
    font-family: "Open Sans", Arial, sans-serif;
    color: var(--ink);
  }
  .sheet {
    position: relative; width: 1200px; height: 720px;
    display: flex; align-items: center; justify-content: center; gap: 40px;
  }
  .card {
    position: relative; width: 540px; height: 309px;
    background: var(--card);
    box-shadow: 0 2px 10px rgba(0,0,0,.12);
    overflow: hidden;
  }

  /* Front */
  .brand {
    position: absolute; left: 36px; top: 62px; width: 210px;
    display: flex; flex-direction: column; align-items: center; gap: 14px;
  }
  .brand-dot {
    width: 70px; height: 70px; border-radius: 50%;
    background: var(--purple);
  }
  .brand-name {
    font-weight: 400; font-size: 46px; letter-spacing: 4px;
    color: var(--purple); line-height: 1;
  }
  .divider {
    position: absolute; left: 262px; top: 28px; width: 1px; height: 140px;
    background: var(--rule);
  }
  .contact { position: absolute; left: 280px; top: 24px; }
  .contact-name { font-weight: 700; font-size: 17px; color: var(--purple); line-height: 1.2; }
  .contact-title { font-size: 12px; color: var(--ink); margin-bottom: 10px; }
  .contact-list { list-style: none; }
  .contact-list li {
    display: flex; align-items: center; gap: 7px;
    font-size: 12px; line-height: 1.85; color: var(--ink);
  }
  .contact-icon { width: 12px; height: 12px; flex: none; }
  .contact-address { font-size: 12px; margin-top: 10px; }
  .swoosh { position: absolute; left: 0; top: 0; width: 540px; height: 309px; }

  /* Back */
  .appointment {
    position: absolute; inset: 0; padding: 58px 36px 0;
    text-align: center;
  }
  .appointment-heading {
    font-weight: 700; font-size: 15px; color: var(--purple);
    letter-spacing: .3px; margin-bottom: 20px;
  }
  .field-row {
    display: flex; align-items: flex-end; gap: 6px;
    font-size: 14px; color: var(--ink); margin-bottom: 18px; text-align: left;
  }
  .field-line { flex: 1; border-bottom: 1px solid var(--grey); height: 16px; }
  .field-line.short { flex: .8; }
  .hours { font-size: 15px; line-height: 1.55; color: var(--ink); margin-top: 10px; }
  .cancel-note { font-size: 14px; color: var(--grey); margin-top: 20px; }
</style>
</head>
<body>
<main class="sheet">

  <section class="card card-front" aria-label="Business card front">
    <div class="brand">
      <span class="brand-dot" aria-hidden="true"></span>
      <span class="brand-name">LUNORA</span>
    </div>
    <span class="divider" aria-hidden="true"></span>
    <div class="contact">
      <p class="contact-name">Your Name</p>
      <p class="contact-title">Title</p>
      <ul class="contact-list">
        <li>
          <svg class="contact-icon" viewBox="0 0 12 12" aria-hidden="true"><circle cx="6" cy="6" r="6" fill="var(--purple)"/><path d="M4 3.2 5 4.6 4.5 5.3c.4.9 1.1 1.6 2 2l.7-.5 1.4 1-.6 1c-2.4-.2-4.3-2.1-4.5-4.5z" fill="#fff"/></svg>
          555.201.0148
        </li>
        <li>
          <svg class="contact-icon" viewBox="0 0 12 12" aria-hidden="true"><circle cx="6" cy="6" r="6" fill="var(--purple)"/><rect x="3" y="4" width="6" height="4.2" fill="#fff"/><path d="M3 4 6 6.4 9 4" fill="none" stroke="var(--purple)" stroke-width=".8"/></svg>
          info@lunoramassagestudio.example
        </li>
        <li>
          <svg class="contact-icon" viewBox="0 0 12 12" aria-hidden="true"><circle cx="6" cy="6" r="6" fill="var(--purple)"/><g fill="none" stroke="#fff" stroke-width=".8"><circle cx="6" cy="6" r="3.4"/><ellipse cx="6" cy="6" rx="1.5" ry="3.4"/><path d="M2.6 6h6.8"/></g></svg>
          www.lunoramassagestudio.example
        </li>
      </ul>
      <p class="contact-address">1475 E Alder Ave, Halvern, ST 00417</p>
    </div>
    <svg class="swoosh" viewBox="0 0 540 309" aria-hidden="true">
      <path d="M0 262 C150 230 320 262 540 186 L540 192 C320 272 150 244 0 276 Z" fill="var(--charcoal)"/>
      <path d="M0 286 C150 252 330 274 540 198 L540 309 L0 309 Z" fill="var(--purple)"/>
    </svg>
  </section>

  <section class="card card-back" aria-label="Business card back, appointment reminder">
    <div class="appointment">
      <h2 class="appointment-heading">YOUR APPOINTMENT</h2>
      <div class="field-row">
        <span>Name :</span><span class="field-line"></span>
        <span>Time :</span><span class="field-line short"></span>
        <span>am / pm</span>
      </div>
      <div class="field-row">
        <span>Date :</span><span class="field-line"></span>
      </div>
      <p class="hours">Wed - Sat 9am - 7pm Sun 11am-4pm<br>(Appointments required) No walk-ins please.</p>
      <p class="cancel-note">We appreciate a 24 hr. notice for cancellations</p>
    </div>
  </section>

</main>
</body>
</html>
```